Travolinex Web Design

We would like to have our website designed and coded. It will be a display only website - no input or output functionality. It's a fairly simple structure with not many pages, but we would like some professional design and creative elements added in to make the site attractive and sharp. I have attached a presentation with the page and content layout. Where images are included in the presentation, those are concepts that you can reorganize or layout in any way that you think looks best. Same with the wheel of services on the incubator page, and the bullet points listed on the accelerator page.

```html
<!DOCTYPE html>
<html lang="en">
<head>
<meta charset="utf-8">
<title>Travolinex</title>
<link href="https://fonts.googleapis.com/css2?family=Montserrat:wght@500;600&family=Questrial&display=swap" rel="stylesheet">
<style>
:root{
  --navy:#0e4a6e;
  --band:#1b5a82;
  --blue:#1d5f8a;
  --grey:#6b6b6b;
  --card:#656565;
  --text:#6a6a6a;
  --white:#ffffff;
  --field:#8a8a8a;
}
*{margin:0;padding:0;box-sizing:border-box}
html,body{width:1200px;height:3176px;overflow:hidden;background:var(--white)}
body{position:relative;font-family:"Questrial",sans-serif;color:var(--text)}
.abs{position:absolute}
.head-font{font-family:"Montserrat",sans-serif}

/* header */
.site-header{left:0;top:0;width:1200px;height:75px;background:var(--navy)}
.brand{left:200px;top:24px;font-family:"Montserrat",sans-serif;font-weight:600;font-size:22px;letter-spacing:1px;color:var(--white)}
.nav{top:30px;font-size:13px;color:var(--white)}
.contact-btn{left:869px;top:22px;width:130px;height:31px;border-radius:16px;background:var(--grey);color:var(--white);font-size:13px;text-align:center;line-height:31px}

/* hero */
.hero{left:0;top:75px;width:1200px;height:500px;overflow:hidden;background:linear-gradient(180deg,#a9a9a9 0%,#8c8c8c 45%,#b5b1ab 100%)}
.hero-wordmark{left:200px;top:262px;width:800px;text-align:center;font-family:"Montserrat",sans-serif;font-weight:600;font-size:108px;letter-spacing:2px;color:var(--blue);line-height:1}

/* intro */
.intro-photo{left:46px;top:666px;width:291px;height:291px;border-radius:50%;background:linear-gradient(135deg,#4d8fb8 0%,#9aa4ad 60%,#5b86a3 100%)}
.intro-lead{left:407px;top:658px;width:595px;font-size:18.5px;line-height:22.5px;color:var(--navy)}
.intro-body{left:407px;width:595px;font-size:12.3px;line-height:18.8px}
.services{left:407px;top:925px;list-style:none;font-size:12.3px;line-height:18.8px;color:var(--navy)}
.services li{padding-left:22px;position:relative}
.services li::before{content:"";position:absolute;left:0;top:6px;width:8px;height:8px;border-radius:50%;background:#5d7d92}

/* dubai band */
.dubai-band{left:0;top:1151px;width:1200px;height:456px;background:var(--band)}
.dubai-small{left:200px;top:1207px;font-size:22px;color:var(--white);font-family:"Montserrat",sans-serif;font-weight:500}
.dubai-big{left:198px;top:1238px;font-size:74px;font-weight:600;color:var(--white);font-family:"Montserrat",sans-serif;line-height:1}
.dubai-cover{left:200px;top:1318px;font-size:35px;line-height:45px;font-weight:500;color:var(--white);font-family:"Montserrat",sans-serif}
.story{left:525px;top:1210px;width:475px;list-style:none;color:var(--white);font-size:12.3px;line-height:15px}
.story li{position:relative;padding-left:37px}
.story li::before{content:"";position:absolute;left:2px;top:0;width:17px;height:17px;border-radius:50%;background:var(--white)}

/* service cards */
.card{top:1670px;width:362px;height:300px;background:var(--card)}
.card-tab{top:1688px;width:150px;height:36px;border-radius:0 18px 18px 0;background:var(--navy);color:var(--white);font-size:15px;line-height:36px;padding-left:36px}
.card-title{top:1741px;width:310px;font-family:"Montserrat",sans-serif;font-weight:500;font-size:18px;line-height:22px;color:var(--white)}
.card-text{width:305px;font-size:10px;line-height:15px;color:#eaeaea}
.card-corner{top:1908px;width:74px;height:74px}

/* distribution */
.dist-label{left:200px;top:2068px;font-size:14px;color:var(--grey);font-family:"Montserrat",sans-serif;font-weight:500}
.dist-title{left:200px;top:2094px;font-family:"Montserrat",sans-serif;font-weight:600;font-size:30px;line-height:36px;color:var(--navy)}
.dist-text{left:200px;width:395px;font-size:12.3px;line-height:18.8px}
.read-more{left:201px;top:2351px;width:111px;height:32px;border-radius:16px;background:var(--grey);color:var(--white);font-size:13px;text-align:center;line-height:32px}
.diamond{width:150px;height:150px;transform:rotate(45deg)}

/* references */
.references{left:0;top:2483px;width:1200px;height:344px;background:var(--navy)}
.ref-title{left:0;top:2538px;width:1200px;text-align:center;font-family:"Montserrat",sans-serif;font-weight:500;font-size:29px;letter-spacing:1px;color:var(--white)}
.ref-tile{width:149px;height:74px;background:var(--white);text-align:center;line-height:74px;font-size:21px;color:var(--navy)}

/* footer */
.site-footer{left:0;top:2827px;width:1200px;height:349px;background:var(--grey)}
.foot-h{top:2886px;font-size:18.5px;color:var(--white);letter-spacing:.5px}
.foot-small{color:var(--white);font-size:10px;line-height:13px}
.social{top:3048px;width:30px;height:30px;border-radius:50%;background:var(--white)}
.social.active{background:var(--navy);border:2px solid var(--white)}
.field{height:24px;background:var(--field);border-radius:3px;color:#e4e4e4;font-size:9.5px;padding:6px 12px}
.send{left:413px;top:3047px;width:99px;height:33px;border-radius:17px;background:var(--navy);color:var(--white);font-size:13px;text-align:center;line-height:33px}
.foot-rule{left:200px;top:3129px;width:800px;height:1px;background:#a8a8a8}
.copyright{left:0;top:3146px;width:1200px;text-align:center;font-size:9.5px;color:var(--white)}
</style>
</head>
<body>

<header class="abs site-header"></header>
<div class="abs brand">TRAVOLINEX</div>
<nav>
  <span class="abs nav" style="left:475px">Incubator</span>
  <span class="abs nav" style="left:560px">Accelerator</span>
  <span class="abs nav" style="left:656px">UAE Distribution</span>
  <span class="abs nav" style="left:779px">References</span>
</nav>
<div class="abs contact-btn">Contact Us</div>

<section class="abs hero" role="img" aria-label="Black and white photograph of a historic fishing village shore with boats blending into the modern city skyline">
  <svg width="1200" height="500" class="abs" style="left:0;top:0">
    <circle cx="950" cy="258" r="282" fill="#9c9c9c" stroke="#d8d8d8" stroke-width="8"/>
  </svg>
</section>
<div class="abs hero-wordmark">TRAVOLINEX</div>

<div class="abs intro-photo" role="img" aria-label="Round photo of the city skyline in blue tones"></div>
<h1 class="abs intro-lead" style="font-weight:400">Travolinex is a global incubator for start-up and early-stage medical device companies and serves as a growth accelerator for more advanced medical device companies.</h1>
<p class="abs intro-body" style="top:738px;width:540px">Located in Dubai Harbour Tech Park, a fully integrated technology park with the aim to foster technology and entrepreneurship, Travolinex provides active operational support to medical device companies through the expertise of highly experienced and well-connected industry veterans.</p>
<p class="abs intro-body" style="top:832px">These veterans serve as mentors, interim-managers or as freelance consultants, enabling medical device companies to outsource key operational functions, lowering monthly operating expenses and minimizing operational risks. Along with the operational support Travolinex provides, we utilize our global network of strategic partners, distributors, manufacturers and healthcare providers to:</p>
<ul class="abs services">
  <li>Raise Capital</li>
  <li>Assist and drive M&amp;A strategies</li>
  <li>Develop global sales and marketing strategies</li>
  <li>Build and expand distribution channels</li>
  <li>Source suppliers and assist in outsourcing production</li>
  <li>Support in Regulatory Affairs</li>
</ul>
<p class="abs intro-body" style="top:1057px">Travolinex helps your business minimize operational risk, operate more cost-effective, grow faster and increase profitability.</p>

<section class="abs dubai-band" role="img" aria-label="Faint world map with connecting network lines"></section>
<div class="abs dubai-small">LOCATED IN</div>
<div class="abs dubai-big">DUBAI</div>
<div class="abs dubai-cover">COVERING THE<br>WORLD</div>
<ul class="abs story">
  <li style="margin-bottom:15px">The story of Dubai - from a small fishing village of palm frond huts to the most modern city in the world.</li>
  <li style="margin-bottom:15px">In a matter of 20 years Dubai has shown the world what ambition, vision and leadership, coupled with determination to overcome the odds, can achieve.</li>
  <li style="margin-bottom:15px">The story of Dubai symbolizes the ambition of many corporations and leaders around the globe.</li>
  <li style="margin-bottom:15px">We are proud to call Dubai our home for the past 20 years, having witnessed the most dynamic phase of that growth.</li>
  <li style="margin-bottom:15px">The Dubai story has inspired the founding of Travolinex. A globally connected company, driven by passionate medical device industry experts, aiming for the exceptional and never the average.</li>
  <li style="margin-bottom:15px">Connecting the global medical device world, helping young and established medical device companies to accelerate. Always with the goal to become the best - as impossible as it might seem.</li>
  <li>Dubai has shown the world - It is not impossible!</li>
</ul>

<article>
  <div class="abs card" style="left:212px"></div>
  <div class="abs card-tab" style="left:200px">Incubator</div>
  <h2 class="abs card-title" style="left:238px">GLOBAL MEDICAL DEVICE INCUBATOR</h2>
  <p class="abs card-text" style="left:238px;top:1800px">Travolinex serves as an incubator for start-up and early-stage medical device companies. The most recent COVID pandemic has shown that permanent workspaces have lost their importance. Many global technology incubators are focused on providing office space and a geographically, centralized ecosystem of industry specific companies. However, today's world of global connectivity offers the opportunity for a much farther-reaching technology ecosystem than the location of one office and technology park can ever offer ...</p>
  <svg class="abs card-corner" style="left:513px" viewBox="0 0 74 74"><path d="M74 0V74H0Z" fill="#0e4a6e"/><path d="M42 53h14M51 48l5 5-5 5" stroke="#fff" stroke-width="1.6" fill="none"/></svg>
</article>
<article>
  <div class="abs card" style="left:625px"></div>
  <div class="abs card-tab" style="left:613px;width:200px">Growth Accelerator</div>
  <h2 class="abs card-title" style="left:650px">GROWTH ACCELERATOR</h2>
  <p class="abs card-text" style="left:650px;top:1777px">Managing growth is one of the most difficult tasks any company leader has to manage. Growth needs investment and often requires entering new markets. New markets mean new entry barriers, a new competitive landscape, new customer demands...</p>
  <p class="abs card-text" style="left:650px;top:1867px">The value proposition that works well in a home market may not be valued the same in a different country. This may be due to the way healthcare systems operate or requirements of technology and expertise may be different ...</p>
  <svg class="abs card-corner" style="left:926px" viewBox="0 0 74 74"><path d="M74 0V74H0Z" fill="#0e4a6e"/><path d="M42 53h14M51 48l5 5-5 5" stroke="#fff" stroke-width="1.6" fill="none"/></svg>
</article>

<div class="abs dist-label">UAE DISTRIBUTION</div>
<h2 class="abs dist-title">UAE MEDICAL DEVICE<br>DISTRIBUTION</h2>
<p class="abs dist-text" style="top:2175px">Travolinex distributes medical devices through a direct sales force in the United Arab Emirates.</p>
<p class="abs dist-text" style="top:2231px">Our focus is the promotion of our portfolio companies, introducing highly innovative medical devices into the UAE health-care market. This sales channel provides a footprint for our port-folio companies in the Middle East, a $ 30 Billion market for medical devices. Our sales force is specialized ...</p>
<div class="abs read-more">Read More</div>
<div class="abs diamond" style="left:703px;top:2065px;background:linear-gradient(180deg,#6fa3d6,#b9a888)" role="img" aria-label="Photo of a tall tower against a blue sky"></div>
<div class="abs diamond" style="left:640px;top:2237px;background:linear-gradient(180deg,#5d92c8,#2a5f86)" role="img" aria-label="Photo of waterfront skyscrapers"></div>
<div class="abs diamond" style="left:818px;top:2176px;background:linear-gradient(180deg,#8fb6dd,#c7a36a)" role="img" aria-label="Photo of a traditional sand-coloured fort"></div>

<section class="abs references"></section>
<h2 class="abs ref-title">REFERENCES</h2>
<div class="abs ref-tile" style="left:200px;top:2599px">Corvel Rental</div>
<div class="abs ref-tile" style="left:362px;top:2599px">Medoria</div>
<div class="abs ref-tile" style="left:525px;top:2599px">Qasira</div>
<div class="abs ref-tile" style="left:687px;top:2599px">Helvand Group</div>
<div class="abs ref-tile" style="left:850px;top:2599px">Surgeta</div>
<div class="abs ref-tile" style="left:281px;top:2686px">cardilo</div>
<div class="abs ref-tile" style="left:444px;top:2686px">Nervana</div>
<div class="abs ref-tile" style="left:606px;top:2686px">Tovaro</div>
<div class="abs ref-tile" style="left:768px;top:2686px">pulsetra</div>

<footer class="abs site-footer"></footer>
<h3 class="abs foot-h" style="left:200px;font-weight:400">Conatct Us</h3>
<div class="abs" style="left:200px;top:2921px;color:var(--white);font-size:13.5px">Call: 123-456-7890</div>
<div class="abs foot-small" style="left:200px;top:2937px;text-decoration:underline">info@travolinex.com</div>
<div class="abs foot-small" style="left:200px;top:2968px">Address:<br>Lorem ipsum work dammy Address<br>Dammmy Place - Ma-569139</div>
<div class="abs social" style="left:201px"></div>
<div class="abs social active" style="left:239px"></div>
<div class="abs social" style="left:276px"></div>
<div class="abs social" style="left:314px"></div>
<h3 class="abs foot-h" style="left:413px;font-weight:400">Send Us Message</h3>
<div class="abs field" style="left:413px;top:2924px;width:186px">Name</div>
<div class="abs field" style="left:613px;top:2924px;width:186px">Email</div>
<div class="abs field" style="left:813px;top:2924px;width:186px">Phone</div>
<div class="abs field" style="left:413px;top:2961px;width:586px;height:74px">Message</div>
<div class="abs send">Send</div>
<div class="abs foot-rule"></div>
<div class="abs copyright">© 2021 Travolinex. All Rights Reserved.</div>
<svg class="abs" style="left:1088px;top:3117px" width="26" height="28" viewBox="0 0 26 28"><path d="M13 2L2 26l11-7 11 7Z" fill="none" stroke="#fff" stroke-width="2" stroke-linejoin="round"/></svg>

</body>
</html>
```